Hello, I would like a small logo change and template for business cards.
It will be much like the "Les Perles de Mona", with following changes:.
1. The round shape stays the same
2. The color will be the brown version I already have
3. The wording will be "MONA Arrange"

Hello, 

So the "brown" is actually Pantone 126

Good luck

```html
<!DOCTYPE html>
<html lang="en">
<head>
<meta charset="utf-8">
<title>MONA Arrange – Business Card</title>
<link href="https://fonts.googleapis.com/css2?family=Marcellus&family=Lato:wght@400&display=swap" rel="stylesheet">
<style>
  :root {
    --pantone-126: #a3820f;
    --gold-deep: #5a4406;
    --bead-dark: #2a1f05;
    --paper: #f4f3f0;
    --ink-grey: #5b5b5b;
    --backdrop-top: #8d8d8d;
    --backdrop-bottom: #e4e4e4;
    --white: #ffffff;
  }
  * { margin: 0; padding: 0; box-sizing: border-box; }
  html, body { width: 1200px; height: 823px; overflow: hidden; }
  body {
    background: linear-gradient(180deg, var(--backdrop-top) 0%, var(--backdrop-bottom) 100%);
    font-family: "Lato", Arial, sans-serif;
    position: relative;
  }
  .card {
    position: absolute;
    top: 262px;
    width: 520px;
    height: 300px;
    border-radius: 28px;
    overflow: hidden;
    box-shadow: 0 10px 24px rgba(0,0,0,0.28);
  }
  .card--front { left: 50px; }
  .card--back { left: 630px; background: var(--paper); }

  .front-photo {
    position: absolute; inset: 0;
    background:
      radial-gradient(ellipse at 50% 45%, #9c7a14 0%, #806208 45%, var(--gold-deep) 80%, var(--bead-dark) 100%);
  }
  .front-url {
    position: absolute; left: 0; right: 0; top: 140px;
    text-align: center;
    font-family: "Marcellus", Georgia, serif;
    font-size: 19px;
    color: var(--white);
    letter-spacing: 0.3px;
  }
  .front-url strong { font-weight: 400; font-size: 21px; }

  .holder { position: absolute; left: 40px; top: 72px; }
  .holder-name { font-size: 14px; color: var(--pantone-126); letter-spacing: 0.3px; }
  .holder-role { font-size: 11px; color: var(--ink-grey); margin-top: 2px; }

  .contact-list { position: absolute; left: 40px; top: 150px; list-style: none; }
  .contact-item {
    display: flex; align-items: flex-start; gap: 8px;
    font-size: 11.5px; line-height: 15px; color: var(--ink-grey);
    margin-bottom: 3px;
  }
  .contact-icon { width: 10px; height: 12px; flex: none; margin-top: 1px; fill: var(--pantone-126); }

  .brand-seal {
    position: absolute; right: 44px; top: 58px;
    width: 190px; height: 190px; border-radius: 50%;
    background: var(--pantone-126);
    display: flex; align-items: center; justify-content: center;
  }
  .brand-name {
    display: flex; flex-direction: column; align-items: center;
    font-family: "Marcellus", Georgia, serif;
    font-size: 28px; line-height: 1.15;
    color: var(--white); letter-spacing: 1px;
    text-align: center; white-space: nowrap;
  }
</style>
</head>
<body>

  <section class="card card--front">
    <div class="front-photo" role="img" aria-label="Golden-toned photograph of scattered pearl beads framing the centre"></div>
    <p class="front-url">www.<strong>PerlesMona</strong>.ro</p>
  </section>

  <section class="card card--back">
    <div class="holder">
      <p class="holder-name">CARDHOLDER NAME</p>
      <p class="holder-role">Designation</p>
    </div>

    <ul class="contact-list">
      <li class="contact-item">
        <svg class="contact-icon" viewBox="0 0 10 12"><path d="M5 0a4 4 0 0 0-4 4c0 3 4 8 4 8s4-5 4-8a4 4 0 0 0-4-4zm0 5.5A1.5 1.5 0 1 1 5 2.5a1.5 1.5 0 0 1 0 3z"/></svg>
        <span>0101 Avenue, Suite No. 123,<br>Your City, Country</span>
      </li>
      <li class="contact-item">
        <svg class="contact-icon" viewBox="0 0 10 12"><circle cx="5" cy="6" r="5"/><path d="M3 3.5l1.2-.3.8 1.6-.8.6c.4.9 1 1.5 1.8 1.8l.6-.8 1.6.8-.3 1.2C5.5 8.4 3.2 6 3 3.5z" fill="#f4f3f0"/></svg>
        <span>+012 345 6789</span>
      </li>
      <li class="contact-item">
        <svg class="contact-icon" viewBox="0 0 10 12"><rect x="2" y="1" width="6" height="4"/><rect x="0" y="5" width="10" height="6" rx="1"/></svg>
        <span>+012 345 6780</span>
      </li>
      <li class="contact-item">
        <svg class="contact-icon" viewBox="0 0 10 12"><rect x="0" y="3" width="10" height="7" rx="1"/><path d="M0.5 3.5L5 7l4.5-3.5" stroke="#f4f3f0" fill="none"/></svg>
        <span>cardholder.name@perlesmona.ro</span>
      </li>
    </ul>

    <div class="brand-seal">
      <p class="brand-name"><span>MONA</span><span>Arrange</span></p>
    </div>
  </section>

</body>
</html>
```